Looking for a creative label design for our retail coffee bags

We are a coffee manufacturer (coffee roaster) looking to re-brand our retail label for our coffee bags. Our main coffee blend that we sell is our Colombian Supremo Blend. You can use this name when creating the label. We are going for a look that represents our company as a coffee roaster. Please reference our website (www.brindlemoorroasters.com) and our Facebook page to learn more about our company and to give you more inspiration on creating this design.

Target Market(s)

Retail customers/grocery stores

Industry/Entity Type

Manufacturer

Requirements
Must have
• The size of the label has to be 3" width x 4" height

Logo must be Black
Nice to have
• We currently incorporate a color on our labels for each blend. For example, Colombian Supremo Blend (royal blue), Decaffeinated Blend (red), Breakfast Blend (green), Flavored coffees (gold).

Rustic/vintage style

```html
<!DOCTYPE html>
<html lang="en">
<head>
<meta charset="utf-8">
<title>Brindlemoor Roasters – Retail Coffee Labels</title>
<link rel="stylesheet" href="https://fonts.googleapis.com/css2?family=Alegreya+Sans+SC:wght@800&family=Pinyon+Script&display=swap">
<style>
  :root {
    --paper: #ffffff;
    --frame: #9a9a9a;
    --ink: #000000;
    --royal-blue: #272262;
    --forest-green: #066b3b;
    --brick-red: #921a1f;
    --gold: #f6941e;
  }
  * { box-sizing: border-box; margin: 0; padding: 0; }
  html, body { width: 1200px; height: 1100px; overflow: hidden; }
  body { background: var(--paper); }
  .sheet {
    position: relative;
    width: 1200px; height: 1100px;
    border: 1px solid var(--frame);
    background: var(--paper);
  }
  .label {
    position: absolute;
    width: 331px; height: 442px;
    border-radius: 21px;
    background: var(--blend);
    overflow: hidden;
  }
  .label--colombian { left: 242px; top: 88px;  --blend: var(--royal-blue); }
  .label--breakfast { left: 615px; top: 88px;  --blend: var(--forest-green); }
  .label--decaf     { left: 242px; top: 581px; --blend: var(--brick-red); }
  .label--flavored  { left: 615px; top: 581px; --blend: var(--gold); }

  .brand-strip {
    position: absolute;
    left: 76px; top: 0;
    width: 183px; height: 150px;
    background: var(--paper);
    display: flex; flex-direction: column;
    align-items: center; justify-content: center;
    gap: 8px;
  }
  .brand-dot {
    width: 30px; height: 30px;
    border-radius: 50%;
    background: var(--ink);
  }
  .brand-name {
    font-family: "Alegreya Sans SC", sans-serif;
    font-weight: 800;
    font-size: 19px;
    line-height: 1.05;
    color: var(--ink);
    text-align: center;
  }

  .name-panel {
    position: absolute;
    left: 19px; top: 140px;
    width: 296px; height: 165px;
    background: var(--paper);
    border-radius: 12px;
    text-align: center;
  }
  .tagline {
    font-family: "Pinyon Script", cursive;
    font-size: 28px;
    line-height: 1;
    color: var(--ink);
    margin-top: 12px;
  }
  .blend-name {
    font-family: "Alegreya Sans SC", sans-serif;
    font-weight: 800;
    font-size: 38px;
    line-height: 0.98;
    color: var(--ink);
    margin-top: 6px;
    letter-spacing: 0.5px;
  }
  .blend-name--long { font-size: 33px; }

  .bean-art {
    position: absolute;
    left: 76px; top: 305px;
    width: 239px; height: 137px;
    background: linear-gradient(160deg, var(--paper) 0%, var(--paper) 18%, var(--blend) 62%);
    clip-path: polygon(0 0, 100% 0, 100% 55%, 28% 100%, 0 70%);
  }
</style>
</head>
<body>
<main class="sheet">

  <section class="label label--colombian">
    <div class="brand-strip"><span class="brand-dot"></span><p class="brand-name">Brindlemoor<br>Roasters</p></div>
    <div class="name-panel">
      <p class="tagline">Fresh roasted</p>
      <h2 class="blend-name blend-name--long">Colombian<br>Supremo Blend</h2>
    </div>
    <div class="bean-art" role="img" aria-label="Coffee bean with rising steam illustration in royal blue"></div>
  </section>

  <section class="label label--breakfast">
    <div class="brand-strip"><span class="brand-dot"></span><p class="brand-name">Brindlemoor<br>Roasters</p></div>
    <div class="name-panel">
      <p class="tagline">Fresh roasted</p>
      <h2 class="blend-name">Breakfast<br>Blend</h2>
    </div>
    <div class="bean-art" role="img" aria-label="Coffee bean with rising steam illustration in green"></div>
  </section>

  <section class="label label--decaf">
    <div class="brand-strip"><span class="brand-dot"></span><p class="brand-name">Brindlemoor<br>Roasters</p></div>
    <div class="name-panel">
      <p class="tagline">Fresh roasted</p>
      <h2 class="blend-name">Decaffeinated<br>Blend</h2>
    </div>
    <div class="bean-art" role="img" aria-label="Coffee bean with rising steam illustration in red"></div>
  </section>

  <section class="label label--flavored">
    <div class="brand-strip"><span class="brand-dot"></span><p class="brand-name">Brindlemoor<br>Roasters</p></div>
    <div class="name-panel">
      <p class="tagline">Fresh roasted</p>
      <h2 class="blend-name">Flavored<br>coffees</h2>
    </div>
    <div class="bean-art" role="img" aria-label="Coffee bean with rising steam illustration in gold"></div>
  </section>

</main>
</body>
</html>
```